TheGlowFrame.net

TheGlowFrame.net
Open Globe Snap Salon of pictures of love for all to enjoy
My goal is to create a website that is designed to be an online art gallery of photos that display what love looks like from all over the world. People will submit an image; write a short quote about why their image represents love
I Love THIS website:
http://markwellory.example/
Please create something like this!!!
User Functionality:
Users must be able to do the following:
• Upload one photo
• Write a brief quote
• Share on their social media site
• Other users can like and share posted image
Backend:
• Site owner must be able to choose which images are uploaded. After user uploads image to site, admin will receive notice of the upload, and make sure the image is not unappropriated or spam. That would be the control functionality.
• At the bottom of the site a contact us, that will send e-mail to admin for any user related questions
Design Functionality:
Website should only be one, simple, elegant, page of photos.
Social Media:
Social media buttons should be small, at the corner of each submitted image
I Love THIS website:
http://markwellory.example/
Homepage: I like the layout and design you have now. Each square/image will have the following social media options, friendloop,chirpline,and Snapgrid. Below each photo their will be a caption that described each photo that appears after you hover over the photo, camera equipment, and a link to the photographer's portfolio/website. There will be able 30-40 images at a time on the homepage, 5-7 photographers at a time.
Featured Photographers:
This is the second page of the website. Here there is a bio of the photographers, how to contact them, and where in the world they are from. The photographers will always be on the page even after their work is taken off the homepage. I will insert links to their personal websites under their bio.
Review/Shop:
Here I will be using affiliated marketing to sell cameras, camera accessories, online photo classes, frames. I will not be selling the pictures featured on the homepage, people will be able to buy directly from the photographer.
Selling: I will be using brimhall partners, and tap vault. I will be installing CoinDrift, but all sales will be they third party vendors
Contact Us:
Here people can inquire about becoming a featured photographer, the company, and anything else
Site Requirements:
Email visitors can join the company mail group.
Target Market(s)
photographers, people who like snapgrid, and boardly
Industry/Entity Type
Marketing
Look and feel

```html
<!DOCTYPE html>
<html lang="en">
<head>
<meta charset="UTF-8">
<title>TheGlowFrame.net</title>
<link rel="stylesheet" href="https://fonts.googleapis.com/css2?family=Source+Sans+3:wght@400;600;700&display=swap">
<style>
  :root{
    --bar:#2a2a2c;
    --bar-text:#ffffff;
    --accent:#29a6cc;
    --red:#e5262c;
    --ink:#333338;
    --body:#4a4a50;
    --button:#1c3856;
    --page:#ffffff;
  }
  *{box-sizing:border-box;margin:0;padding:0}
  html,body{width:800px;height:1200px;overflow:hidden;background:var(--page)}
  body{font-family:"Source Sans 3",Arial,sans-serif;color:var(--ink);position:relative}

  .top-bar{position:absolute;top:0;left:0;width:800px;height:75px;background:var(--bar);display:flex;align-items:center;justify-content:space-between;padding:0 46px 0 138px}
  .brand{color:var(--bar-text);font-weight:700;font-size:20px;letter-spacing:-.2px}
  .account{display:flex;align-items:center;font-size:16px;color:var(--bar-text)}
  .account .divider{width:1px;height:18px;background:#8a8a8e;margin:0 10px}
  .account .sign-up{color:var(--accent)}

  .hero{position:absolute;top:75px;left:0;width:800px;height:305px;overflow:hidden;
    background:linear-gradient(90deg,#d9e9a8 0%,#bcd77a 30%,#a9cc63 55%,#b7d27c 75%,#d4e3a9 100%)}
  .hero-photo{position:absolute;inset:0;background:
     radial-gradient(ellipse at 68% 35%,rgba(250,245,230,.9) 0%,rgba(250,245,230,0) 38%),
     linear-gradient(180deg,rgba(255,255,245,.55) 0%,rgba(255,255,255,0) 45%,rgba(110,160,40,.35) 100%)}
  .hero-caption{position:absolute;left:138px;top:80px;width:330px}
  .hero-caption h2{color:var(--red);font-size:27px;font-weight:600;line-height:1.1;margin-bottom:8px}
  .hero-caption p{font-size:21px;line-height:1.3;color:#2a2a2a}
  .hero-arrow{position:absolute;top:120px}
  .hero-arrow.prev{left:92px}
  .hero-arrow.next{right:92px}
  .hero-shadow{position:absolute;top:378px;left:0;width:800px;height:22px}

  .welcome{position:absolute;top:408px;left:0;width:800px;text-align:center}
  .welcome h1{font-size:30px;font-weight:600;color:var(--ink);margin-bottom:12px}
  .welcome p{font-size:20px;line-height:1.3;color:var(--body);width:560px;margin:0 auto}

  .gallery{position:absolute;top:552px;left:139px;display:grid;grid-template-columns:repeat(3,163px);grid-auto-rows:163px;gap:15px 15px}
  .tile{display:block}
  .t1{background:linear-gradient(160deg,#8fb1cf,#7b6a43 60%,#5b4a2c)}
  .t2{background:linear-gradient(180deg,#e9a94d,#d07a2a 55%,#3c2f2a)}
  .t3{background:linear-gradient(180deg,#5f97d6,#b18a5c 60%,#7a5a3a)}
  .t4{background:linear-gradient(180deg,#6fb0e5,#c9a363 60%,#9e7a44)}
  .t5{background:radial-gradient(circle at 50% 45%,#f2d6c6,#d49a8c 55%,#6f9a3d)}
  .t6{background:linear-gradient(180deg,#7daa4e,#446d2b 60%,#2b4a1f)}
  .t7{background:linear-gradient(180deg,#e7a24a,#b1693a 55%,#4c3428)}
  .t8{background:linear-gradient(180deg,#8db4cc,#6b7f6b 55%,#4a4d3a)}
  .t9{background:linear-gradient(180deg,#7fa2b3,#5c8aa9 50%,#c6a067)}

  .load-more{position:absolute;top:1088px;left:333px;width:142px;height:45px;background:var(--button);color:#fff;border:0;font-family:inherit;font-size:15px;font-weight:600;border-radius:2px}

  .site-footer{position:absolute;bottom:0;left:0;width:800px;height:45px;background:var(--bar);display:flex;align-items:center;justify-content:space-between;padding:0 46px 0 138px}
  .copyright{color:#d8d8d8;font-size:10px}
  .social{display:flex;gap:8px}
  .social span{width:17px;height:17px;border-radius:50%;border:1.5px solid #cfcfcf;display:block}
</style>
</head>
<body>
  <header class="top-bar">
    <div class="brand">TheGlowFrame.net</div>
    <nav class="account">
      <span class="sign-in">Sign in</span>
      <span class="divider"></span>
      <span class="sign-up">Sign up</span>
    </nav>
  </header>

  <section class="hero">
    <div class="hero-photo" role="img" aria-label="Young woman lying in a sunny grass meadow with an open book"></div>
    <div class="hero-caption">
      <h2>Pellentesque accumsan</h2>
      <p>Lorem ipsum is a dummy text only. Dolor sit amet, consectetur adipiscing elit</p>
    </div>
    <svg class="hero-arrow prev" width="22" height="40" viewBox="0 0 22 40" aria-hidden="true"><path d="M18 4 L4 20 L18 36" fill="none" stroke="#ffffff" stroke-width="3" opacity=".85"/></svg>
    <svg class="hero-arrow next" width="22" height="40" viewBox="0 0 22 40" aria-hidden="true"><path d="M4 4 L18 20 L4 36" fill="none" stroke="#ffffff" stroke-width="3" opacity=".85"/></svg>
  </section>
  <svg class="hero-shadow" viewBox="0 0 800 22" preserveAspectRatio="none" aria-hidden="true">
    <defs><radialGradient id="shade" cx="50%" cy="0%" r="60%"><stop offset="0" stop-color="#000" stop-opacity=".35"/><stop offset="1" stop-color="#000" stop-opacity="0"/></radialGradient></defs>
    <path d="M0 0 L800 0 Q400 28 0 0 Z" fill="url(#shade)"/>
  </svg>

  <section class="welcome">
    <h1>Welcome to TheGlowFrame.net</h1>
    <p>Lorem ipsum is a dummy text only. Dolor sit amet, consectetur adipiscing elit. Nullam felis mauris, eleifend ac rhoncus non, lobortis at diam.</p>
  </section>

  <main class="gallery">
    <div class="tile t1" role="img" aria-label="Old spreading tree under a blue sky"></div>
    <div class="tile t2" role="img" aria-label="Sunset over hazy mountain ridges"></div>
    <div class="tile t3" role="img" aria-label="Couple embracing among red desert rocks"></div>
    <div class="tile t4" role="img" aria-label="Runner leaping across a sunny field"></div>
    <div class="tile t5" role="img" aria-label="Close-up of an ant on a pink balloon"></div>
    <div class="tile t6" role="img" aria-label="Couple sitting by a forest stream"></div>
    <div class="tile t7" role="img" aria-label="Man with a horse at golden hour"></div>
    <div class="tile t8" role="img" aria-label="Photographer with a camera outdoors"></div>
    <div class="tile t9" role="img" aria-label="Child holding a painted globe toy"></div>
  </main>

  <button class="load-more">Load more pictures</button>

  <footer class="site-footer">
    <p class="copyright">Copyright © TheGlowFrame.net. All Rights Reserved. 2014</p>
    <div class="social" aria-label="Social links">
      <span aria-label="Email"></span>
      <span aria-label="friendloop"></span>
      <span aria-label="Snapgrid"></span>
      <span aria-label="chirpline"></span>
    </div>
  </footer>
</body>
</html>
```